I need a cd cover for a new pop rock album called "Letters from the tin harbour"
The main color of the artwork shall obviously be orange. The artwork shouldn't be too "obvious", but it would be better something a bit abstract.
Please remember that it is a Music Cd Cover, so do not send business logo or advertisement images.

It's a pop rock album, so the target customers are young and adult people from 15-60 years old

• Orange as main colour
The Artist name is: Tomas Verhelst
The Title: Letters from the tin harbour
• Not too cheesy or dreamy images please. No simple sunset or sunrise pics

```html
<!DOCTYPE html>
<html lang="en">
<head>
<meta charset="utf-8">
<title>Letters from the tin harbour — Tomas Verhelst</title>
<link rel="stylesheet" href="https://fonts.googleapis.com/css2?family=Anton&display=swap">
<style>
  :root {
    --orange: #ff8a00;
    --blue: #056fff;
    --navy: #011027;
    --white: #ffffff;
  }
  html, body {
    margin: 0;
    padding: 0;
    width: 1200px;
    height: 1200px;
    overflow: hidden;
    background: var(--white);
  }
  .cover {
    display: block;
    width: 1200px;
    height: 1200px;
  }
  .band-orange { fill: var(--orange); }
  .band-blue { fill: var(--blue); }
  .band-navy { fill: var(--navy); }
  .divider { fill: var(--white); }
  .album-title,
  .artist-name {
    font-family: "Anton", "Oswald", sans-serif;
    fill: var(--white);
  }
  .album-title { font-size: 132px; }
  .artist-name { font-size: 160px; }
</style>
</head>
<body>
  <svg class="cover" viewBox="0 0 1200 1200" xmlns="http://www.w3.org/2000/svg" role="img" aria-label="Letters from the tin harbour by Tomas Verhelst">
    <rect class="band-orange" x="0" y="0" width="1200" height="445"/>
    <rect class="band-blue" x="0" y="471" width="1200" height="410"/>
    <rect class="band-navy" x="0" y="909" width="1200" height="291"/>

    <text class="album-title" x="45" y="462" textLength="1103" lengthAdjust="spacingAndGlyphs">LETTERS FROM THE TIN HARBOUR</text>
    <rect class="divider" x="0" y="445" width="1200" height="26"/>

    <text class="artist-name" x="26" y="898" textLength="704" lengthAdjust="spacingAndGlyphs">TOMAS VERHELST</text>
    <rect class="divider" x="0" y="881" width="1200" height="28"/>
  </svg>
</body>
</html>
```